Industrial Company Website

We need a Website to highlight 5 different Brands we distribute.

We are Dealers for the following products

1)Velorin Tube a Div of Darvell Ostrick ( HDPE Pipes and Fittings )
Velorin Tube is the largest provider of polyethylene pipe (poly pipe) - HDPE pressure pipe and fittings in North America
Inquire page for web user to request pricing.

2) Brantock Weldline Mfg . ( HDPE Fusion Equipment )'
We like to have a system we are able to list top 25 items with part numbers and cost
that a web user is able to select and add to cart and email a order via the web.

3) Olvane Power ( Gate , Check and Globe Valves )
Sub Category Brands , Tessmark , Varilok , and Hollister Valves

4) Fertani North America Valves
http://www.fertaninorthamerica.example/ita/home.pag

5) Corlett Strainers, Inc. - A worldwide manufacturer of heavy-duty air, lube, fuel, coolant, transmission, and hydraulic filtration products
Within this Tab we like to web user to lookup filters from
http://catalog.corlettstrainer.example/ and able to create a inquire
for our company to send a quote .

6) Hargrove-Tamsin Uniforms
http://www.tamsinwear.example/
http://www.gardlyne.example/fireservice/

http://www.pelstrideboots.example/ (Safety Shoes)

Also we like a Tab for Company Profile , and contact information

We have authorization from all companies listed about to use their logo
under our dealership agreements.
Updates

Hello All ,

Please do not use the Tarvix Oil & Gas Logo.

Please Only use the Logo with the Logo with the M and the Flame and Oil Drop

Rex                                   

Target Market(s)

Target Markets ,: International distributor of pipe, valves, fittings and more
serving the Caribbean and South America .

Target Clients : Oil and Gas , Power Plants and Mining Companies

The Web Address will be www.tarvixsupply.example

Industry/Entity Type

It Company

Requirements
Must have
• Note : This Project will possibly lead to the next stage.
Coded and HTML proof of concept to load live.
I will give the winner first chance to Quote me the completion

Note the Goal is to have a E-Comm. Site , but since we are in Wholesale
and not retail . The E-Cart will no take payment but create an inquire and then send me to my email for processing
Nice to have
• I just had a Logo created by a designer on Graphic hive. I will need to share the logo design for your submission

```html
<!DOCTYPE html>
<html lang="en">
<head>
<meta charset="utf-8">
<title>Corvane International</title>
<link rel="stylesheet" href="https://fonts.googleapis.com/css2?family=Open+Sans:wght@400;600;700&display=swap">
<style>
:root{
  --ink:#333a40;
  --muted:#8a9096;
  --blue:#2f7fc1;
  --blue-dark:#1f5f97;
  --topbar:#2b2f33;
  --footer:#34383c;
  --footer-bottom:#26292c;
  --line:#e3e5e8;
  --white:#ffffff;
}
*{box-sizing:border-box;margin:0;padding:0}
html,body{width:800px;height:1200px;overflow:hidden}
body{font-family:"Open Sans",Arial,sans-serif;color:var(--ink);background:var(--white);position:relative;font-size:11px}
.topbar{position:absolute;left:0;top:0;width:800px;height:22px;background:var(--topbar);color:#c9cdd1;font-size:9px;display:flex;justify-content:flex-end;align-items:center;padding-right:80px;gap:14px}
.header{position:absolute;left:0;top:22px;width:800px;height:78px;background:var(--white)}
.brand{position:absolute;left:88px;top:28px;font-size:15px;font-weight:600;color:var(--ink);white-space:nowrap}
.nav{position:absolute;right:80px;top:18px;display:flex;font-size:11px}
.nav a{display:block;padding:14px 15px;color:var(--ink);text-decoration:none}
.nav a.active{background:#e9ebee;border-bottom:3px solid var(--blue)}
.hero{position:absolute;left:0;top:100px;width:800px;height:295px;background:linear-gradient(180deg,#3a2a14 0%,#8a5a1c 45%,#c98a2a 70%,#4a3520 100%)}
.hero-caption{position:absolute;left:100px;top:180px;display:flex;flex-direction:column;align-items:flex-start;gap:4px}
.hero-caption span{display:block;background:rgba(255,255,255,.93);color:var(--ink);font-size:17px;font-weight:600;padding:5px 10px;line-height:1.3}
.hero-caption em{font-style:normal;color:var(--blue)}
.dots{position:absolute;left:100px;top:268px;display:flex;gap:5px}
.dots i{width:7px;height:7px;border-radius:50%;background:#ddd;display:block}
.dots i:first-child{background:var(--blue)}
.features{position:absolute;left:80px;top:415px;width:640px;display:flex;gap:22px}
.feature{flex:1;position:relative;padding-top:25px}
.feature-icon{position:absolute;left:50%;top:0;margin-left:-25px;width:50px;height:50px;border-radius:50%;background:var(--blue-dark);border:4px solid var(--white);display:flex;align-items:center;justify-content:center;z-index:2}
.feature-box{border:1px solid var(--line);background:var(--white);padding:36px 14px 14px;text-align:center;height:105px}
.feature-box h3{font-size:11px;font-weight:600;margin-bottom:6px}
.feature-box p{font-size:8px;color:var(--muted);line-height:1.45}
.feature.highlight .feature-box{background:var(--blue);color:var(--white);border-color:var(--blue);box-shadow:0 4px 8px rgba(0,0,0,.2)}
.feature.highlight .feature-box p{color:#dbe9f6}
.divider{position:absolute;left:80px;top:590px;width:640px;border-top:1px solid var(--line)}
.section-title{font-size:14px;font-weight:400;color:var(--ink)}
.services{position:absolute;left:80px;top:602px;width:640px}
.services-head{display:flex;justify-content:space-between;align-items:center;margin-bottom:10px}
.arrows{display:flex;gap:6px}
.service-grid{display:flex;gap:12px}
.service{flex:1;text-align:center}
.service-photo{height:95px}
.service h4{font-size:10px;font-weight:600;margin-top:6px}
.service p{font-size:7px;color:var(--muted)}
.welcome{position:absolute;left:80px;top:785px;width:400px;height:160px}
.welcome h2{font-size:15px;font-weight:400;margin-bottom:10px}
.welcome p{font-size:8.5px;color:var(--muted);line-height:1.6}
.btn{display:inline-block;background:var(--blue);color:var(--white);font-size:9px;padding:6px 12px;border-radius:2px}
.welcome .btn{position:absolute;top:135px;left:0}
.quote{position:absolute;left:560px;top:785px;width:160px}
.quote h2{font-size:15px;font-weight:400;margin-bottom:10px}
.field{height:18px;border:1px solid var(--line);font-size:7px;color:var(--muted);padding:3px 6px;margin-bottom:6px}
.field.area{height:34px}
.quote .btn{float:right}
.footer{position:absolute;left:0;top:975px;width:800px;height:185px;background:var(--footer);color:#aeb3b8}
.footer-cols{position:absolute;left:80px;top:22px;width:640px;display:flex;gap:20px}
.footer-col{flex:1;font-size:7.5px;line-height:1.6}
.footer-col.wide{flex:1.6}
.footer-col h5{color:var(--white);font-size:9.5px;font-weight:600;margin-bottom:10px}
.social{display:flex;gap:5px;margin-bottom:12px}
.social i{display:block;width:20px;height:20px;background:var(--blue)}
.subscribe{display:flex;margin-top:6px}
.subscribe span{flex:1;background:var(--white);height:18px;color:var(--muted);padding:3px 6px}
.subscribe b{background:var(--blue);color:var(--white);font-weight:400;padding:3px 8px}
.footer-bottom{position:absolute;left:0;top:1160px;width:800px;height:40px;background:var(--footer-bottom);color:#8d9297;font-size:8px}
.footer-bottom nav{position:absolute;left:80px;top:14px;display:flex;gap:14px}
.footer-bottom p{position:absolute;right:80px;top:14px}
</style>
</head>
<body>
<div class="topbar"><span>Login · Register</span><span>My Account</span><span>My Wishlist</span><span>0 items - $0.00</span></div>

<header class="header">
  <div class="brand">Corvane International</div>
  <nav class="nav">
    <a class="active">Home</a><a>About Us</a><a>Olvane Power</a><a>Profile</a><a>Contact Us</a>
  </nav>
</header>

<section class="hero" role="img" aria-label="Refinery plant lit at night with orange lights">
  <div class="hero-caption">
    <span>Pipe Fittings &amp; More Serving The</span>
    <span>Caribbean &amp; <em>South America</em></span>
  </div>
  <div class="dots"><i></i><i></i><i></i><i></i></div>
</section>

<section class="features">
  <div class="feature">
    <div class="feature-icon"><svg width="22" height="22" viewBox="0 0 22 22"><rect x="2" y="8" width="18" height="6" fill="#fff"/><rect x="1" y="6" width="3" height="10" fill="#fff"/><rect x="18" y="6" width="3" height="10" fill="#fff"/></svg></div>
    <div class="feature-box"><h3>PIPES &amp; FITTINGS</h3><p>High density poly pipe and fittings for pressure lines, stocked and shipped to sites across the region.</p></div>
  </div>
  <div class="feature highlight">
    <div class="feature-icon"><svg width="22" height="22" viewBox="0 0 22 22"><rect x="9" y="3" width="4" height="16" fill="#fff" transform="rotate(45 11 11)"/><circle cx="5" cy="5" r="4" fill="#fff"/><circle cx="17" cy="17" r="3" fill="#fff"/></svg></div>
    <div class="feature-box"><h3>FERTANI NORTH AMERICA</h3><p>Ball valves and actuators for process lines, with full dealer support and fast quotes on request.</p></div>
  </div>
  <div class="feature">
    <div class="feature-icon"><svg width="22" height="22" viewBox="0 0 22 22"><path d="M2 4h18l-7 8v7l-4-2v-5z" fill="#fff"/></svg></div>
    <div class="feature-box"><h3>CORLETT STRAINERS</h3><p>Heavy duty air, lube, fuel and hydraulic filters; look up a part and send us an inquiry for a quote.</p></div>
  </div>
</section>

<div class="divider"></div>

<section class="services">
  <div class="services-head">
    <h2 class="section-title">More Services</h2>
    <div class="arrows">
      <svg width="10" height="10" viewBox="0 0 10 10"><path d="M7 1L3 5l4 4" stroke="#333a40" stroke-width="2" fill="none"/></svg>
      <svg width="10" height="10" viewBox="0 0 10 10"><path d="M3 1l4 4-4 4" stroke="#333a40" stroke-width="2" fill="none"/></svg>
    </div>
  </div>
  <div class="service-grid">
    <div class="service"><div class="service-photo" role="img" aria-label="Industrial plant at dusk" style="background:linear-gradient(180deg,#7f9bb8,#4c5a66)"></div><h4>Lorem Ipsum Dolor</h4><p>Pipe supply</p></div>
    <div class="service"><div class="service-photo" role="img" aria-label="Pipeline in open field" style="background:linear-gradient(180deg,#a9c4dc,#6f7a52)"></div><h4>Sit Amet Consectetur</h4><p>Field work</p></div>
    <div class="service"><div class="service-photo" role="img" aria-label="Drilling rig on site" style="background:linear-gradient(180deg,#c9d3da,#5d6266)"></div><h4>Adipiscing Elit</h4><p>Rig parts</p></div>
    <div class="service"><div class="service-photo" role="img" aria-label="Workers in safety uniforms" style="background:linear-gradient(180deg,#b7a58c,#4f4438)"></div><h4>Labore Et Dolore</h4><p>Uniforms</p></div>
  </div>
</section>

<section class="welcome">
  <h2>Welcome To Corvane International</h2>
  <p>We are an international distributor of pipe, valves, fittings and more, serving oil and gas, power plants and mining companies across the Caribbean and South America. As dealers for leading brands we stock HDPE pipe, fusion equipment, gate, check and globe valves, filtration products and safety uniforms. Send us an inquiry from any product page and our team will reply with pricing and lead times for your project.</p>
  <span class="btn">Read More</span>
</section>

<section class="quote">
  <h2>Get A Quote</h2>
  <div class="field">Enter your name</div>
  <div class="field">Enter your email</div>
  <div class="field area">Enter your message</div>
  <span class="btn">Submit</span>
</section>

<footer class="footer">
  <div class="footer-cols">
    <div class="footer-col">
      <h5>Contact Info</h5>
      1420 Harbor Way<br>Suite 200<br>Doral, FL 33100<br>USA<br>info@corvaneintl.example<br>Phone: (305) 555-0142
    </div>
    <div class="footer-col">
      <h5>About Us</h5>
      Dealer of pipe, valves and fittings for industry, serving clients in the Caribbean and South America since day one.
    </div>
    <div class="footer-col">
      <h5>Company Info</h5>
      Our profile<br>Our brands<br>Careers<br>Shipping terms
    </div>
    <div class="footer-col wide">
      <h5>Stay updated on our Social Network</h5>
      <div class="social"><i></i><i></i><i></i></div>
      <h5>Join Our Newsletter</h5>
      <div class="subscribe"><span>Enter your email</span><b>Subscribe</b></div>
    </div>
  </div>
</footer>
<div class="footer-bottom">
  <nav><span>Home</span><span>About Us</span><span>Olvane Power</span><span>Profile</span><span>Contact Us</span></nav>
  <p>© Copyright 2013 All rights Reserved</p>
</div>
</body>
</html>
```